Investment website design - investing in mutual funds

I need a design of a website (only homepage for now) dedicated to investment in mutual funds. Attached is a mock up with all the elements the homepage design should contain. The homepage should contain a logo in the upper left corner, the domain the website will run on is www.morvatelsko.cz , in the upper right corner there should be 2 buttons or links SIGN UP / SIGN IN. The bottom of the homepage should contain links to ABOUT US, FAQ, PRIVACY POLICY, CONTACT US.
Now the main elements on the homepage
1) Video that will explain how the investment works exactly, under this video we will have 3 illustrated icons like the ones attached (see 2nd attachement) that will show the potential investor what exactly they could get when investing with us (education for kids, happy life after they retire, regular monthly payment for the rest of their life).
2) On the right side next to the video we will have a calculator where a potential investor can play with the numbers, the investor can fill in the MONTHLY PAYMENT that he wants to invest regularly every month, the time frame of the investment - for how long he wants to invest. Once the potential investor selects those 2 variables we will calculate for him 2 options - either he can get a ONE TIME PAYOUT once he reaches his investment horizon or he can get a regular monthly payment for the rest of his life. Under the laculator there will be a button 'I want to invest ->'. The functionality of the calculator should be similar to the calculator that can be found here http://www.brovikbanka.cz/brovik-podilove-fondy/ and https://pelvaro.cz/.
The design should look similar to https://pelvaro.cz/ (font, colors, logo). We prefer white background in the area where we have the video and calculator. We also like the design of www.truvanex.com. Let me know if you have any questions.

```html
<!DOCTYPE html>
<html lang="en">
<head>
<meta charset="utf-8">
<title>morvatelsko – investing in mutual funds</title>
<link href="https://fonts.googleapis.com/css2?family=Roboto+Slab:wght@400;700&display=swap" rel="stylesheet">
<style>
  :root {
    --teal: #43b1bd;
    --teal-dark: #2f8e99;
    --field: #bfe2e5;
    --field-text: #2b8a94;
    --accent: #e9553a;
    --accent-shadow: #2f8e99;
    --footer: #4d4b4e;
    --white: #ffffff;
    --screen: #0f0f10;
    --photo-a: #5b6470;
    --photo-b: #b9b3ad;
  }
  * { box-sizing: border-box; margin: 0; padding: 0; }
  html, body { width: 1200px; height: 635px; overflow: hidden; }
  body { font-family: "Roboto Slab", Georgia, serif; background: var(--white); position: relative; }

  .hero { position: absolute; left: 0; top: 0; width: 1200px; height: 488px; background: var(--teal); }
  .footer { position: absolute; left: 0; top: 488px; width: 668px; height: 147px; background: var(--footer); }
  .benefits { position: absolute; left: 668px; top: 488px; width: 532px; height: 147px; background: var(--white); }

  .brand { position: absolute; left: 58px; top: 13px; color: var(--white); font-weight: 700; font-size: 19px; letter-spacing: 0.2px; }

  .auth { position: absolute; top: 15px; height: 22px; width: 60px; background: var(--accent); color: var(--white);
          font-size: 9px; font-weight: 700; text-transform: uppercase; text-align: center; line-height: 22px;
          text-decoration: none; box-shadow: 3px 3px 0 var(--accent-shadow); }
  .auth.sign-in { left: 1002px; }
  .auth.sign-up { left: 1071px; width: 61px; }

  .monitor { position: absolute; left: 51px; top: 102px; width: 560px; height: 340px; background: var(--screen); border-radius: 11px; }
  .monitor-stand { position: absolute; left: 246px; top: 442px; }
  .video { position: absolute; left: 74px; top: 125px; width: 515px; height: 290px;
           background: linear-gradient(135deg, var(--photo-b) 0%, var(--photo-a) 60%, #2c323b 100%); }
  .play { position: absolute; left: 305px; top: 228px; }

  .calculator { position: absolute; left: 684px; top: 96px; width: 452px; color: var(--white); }
  .calculator h1 { font-size: 29px; font-weight: 700; text-transform: uppercase; letter-spacing: 0.3px; line-height: 1; margin-left: -1px; }
  .field { position: absolute; left: 1px; width: 448px; height: 31px; background: var(--field); color: var(--field-text);
           font-size: 11px; line-height: 31px; padding-left: 12px; }
  .field.monthly-investment { top: 42px; }
  .field.one-time { top: 157px; }
  .field.monthly-payout { top: 218px; }
  .label-length { position: absolute; left: 1px; top: 91px; font-size: 10.5px; font-weight: 700; }
  .slider { position: absolute; left: 1px; top: 116px; }
  .or { position: absolute; left: 1px; top: 197px; font-size: 11px; }
  .invest { position: absolute; left: 258px; top: 273px; width: 187px; height: 40px; background: var(--accent);
            color: var(--white); font-size: 15.5px; text-transform: uppercase; text-align: center; line-height: 40px;
            letter-spacing: 0.3px; text-decoration: none; box-shadow: 6px 6px 0 var(--accent-shadow); }

  .footer-nav { position: absolute; left: 0; top: 74px; width: 650px; display: flex; justify-content: center; gap: 23px; }
  .footer-nav a { color: var(--white); text-decoration: none; font-size: 14.5px; font-weight: 500; }
  .copyright { position: absolute; left: 0; top: 112px; width: 668px; text-align: center; color: var(--white); font-size: 9.5px; padding-right: 0; }

  .benefit { position: absolute; top: 27px; width: 140px; text-align: center; }
  .benefit p { margin-top: 10px; color: var(--accent); font-size: 11px; font-weight: 700; }
  .benefit.kids { left: 54px; }
  .benefit.income { left: 196px; }
  .benefit.retirement { left: 348px; }
</style>
</head>
<body>
  <header class="hero">
    <div class="brand">morvatelsko</div>
    <a class="auth sign-in" href="#">Sign in</a>
    <a class="auth sign-up" href="#">Sign up</a>

    <div class="monitor"></div>
    <div class="video" role="img" aria-label="Explainer video still: two colleagues reviewing charts on a laptop"></div>
    <svg class="play" width="76" height="76" viewBox="0 0 76 76" aria-hidden="true">
      <circle cx="38" cy="38" r="35" fill="none" stroke="#fff" stroke-width="4"/>
      <path d="M30 22 L56 38 L30 54 Z" fill="#fff"/>
    </svg>

    <section class="calculator">
      <h1>Our online calculator</h1>
      <div class="field monthly-investment">Regular monthly investment:</div>
      <div class="label-length">Length of investment</div>
      <svg class="slider" width="452" height="20" viewBox="0 0 452 20" aria-hidden="true">
        <line x1="0" y1="9" x2="452" y2="9" stroke="var(--teal-dark)" stroke-width="2.5"/>
        <line x1="0" y1="9" x2="62" y2="9" stroke="#fff" stroke-width="2.5"/>
        <circle cx="62" cy="9" r="9" fill="#e2f5f6"/>
      </svg>
      <div class="field one-time">One timepayment:</div>
      <div class="or">OR</div>
      <div class="field monthly-payout">Monthly payment:</div>
      <a class="invest" href="#">I want to invest</a>
    </section>
  </header>

  <footer class="footer">
    <nav class="footer-nav">
      <a href="#">About us</a>
      <a href="#">FAQ</a>
      <a href="#">Privacy Policy</a>
      <a href="#">Contact</a>
    </nav>
    <p class="copyright">© 2017 morvatelsko. All rights reserved.</p>
  </footer>

  <svg class="monitor-stand" width="172" height="86" viewBox="0 0 172 86" aria-hidden="true">
    <defs>
      <linearGradient id="stand" x1="0" x2="1">
        <stop offset="0" stop-color="#8d8f93"/>
        <stop offset="0.5" stop-color="#e6e7e9"/>
        <stop offset="1" stop-color="#8d8f93"/>
      </linearGradient>
    </defs>
    <path d="M26 0 H146 L150 70 Q168 76 172 82 H0 Q4 76 22 70 Z" fill="url(#stand)"/>
  </svg>

  <section class="benefits">
    <div class="benefit kids">
      <svg width="80" height="80" viewBox="0 0 80 80" aria-hidden="true">
        <circle cx="40" cy="40" r="38" fill="none" stroke="var(--teal)" stroke-width="3"/>
        <circle cx="40" cy="33" r="9" fill="var(--teal)"/>
        <path d="M40 24 q2 -5 6 -6" stroke="var(--teal)" stroke-width="2" fill="none"/>
        <path d="M26 48 q0 6 6 6 H56 M26 48 q0 -4 6 -4 H56" stroke="var(--teal)" stroke-width="3" fill="none"/>
      </svg>
      <p>Education for kids</p>
    </div>
    <div class="benefit income">
      <svg width="80" height="80" viewBox="0 0 80 80" aria-hidden="true">
        <circle cx="40" cy="40" r="38" fill="none" stroke="var(--teal)" stroke-width="3"/>
        <rect x="24" y="44" width="6" height="10" fill="var(--teal)"/>
        <rect x="33" y="38" width="6" height="16" fill="var(--teal)"/>
        <rect x="42" y="41" width="6" height="13" fill="var(--teal)"/>
        <rect x="51" y="32" width="6" height="22" fill="var(--teal)"/>
        <path d="M24 38 L34 29 L42 34 L55 23" stroke="var(--teal)" stroke-width="3" fill="none"/>
        <path d="M50 22 H57 V29" stroke="var(--teal)" stroke-width="3" fill="none"/>
      </svg>
      <p>Passive income</p>
    </div>
    <div class="benefit retirement">
      <svg width="80" height="80" viewBox="0 0 80 80" aria-hidden="true">
        <circle cx="40" cy="40" r="38" fill="none" stroke="var(--teal)" stroke-width="3"/>
        <circle cx="48" cy="36" r="9" fill="var(--teal)"/>
        <path d="M22 50 Q40 38 58 50 Q40 58 22 50 Z" fill="var(--teal)"/>
        <path d="M33 46 L35 26" stroke="var(--teal)" stroke-width="2.5"/>
        <path d="M35 26 q-7 -2 -10 3 M35 26 q7 -3 10 2 M35 26 q-2 -6 -7 -6" stroke="var(--teal)" stroke-width="2.5" fill="none"/>
      </svg>
      <p>Happy retirment</p>
    </div>
  </section>
</body>
</html>
```